Southport Billboard for Hiring more CDL drivers

I need a catch design for a bill board (size 10ft by 36 ft) to catch the attention for semi truck drivers.
In the design I want it to include:
-My company logo along with my website(brisklanefreighters.com) and my number(503-217-6095) for contact info.
-I also need it to say earn up to $90,000 a year
-I will send a few photos to choose from
-I need the logo to look clean and simple! I don't want it to be cluttered just clean, simple and catchy.!

Target Market(s)

CDL Class A holders
Semi Truck Drivers

Industry/Entity Type

Trucking Company

Font styles to use
Other font styles liked:
• a font to match my logo

Requirements
Must have
• "Make up to $90,000"
"brisklanefreighters.com"
"503-217-6095"

```html
<!DOCTYPE html>
<html lang="en">
<head>
<meta charset="utf-8">
<title>Brisk Lane Freighters – Now Hiring Billboard</title>
<link href="https://fonts.googleapis.com/css2?family=Anton&family=Open+Sans:ital,wght@1,700&display=swap" rel="stylesheet">
<style>
  :root {
    --page: #e9edf0;
    --forest: #0f2a1c;
    --forest-deep: #0b2216;
    --orange: #c9650f;
    --white: #ffffff;
    --sky: #7ea4bf;
    --rock: #7a5540;
    --asphalt: #3d4043;
  }
  * { margin: 0; padding: 0; box-sizing: border-box; }
  html, body {
    width: 1200px;
    height: 1173px;
    overflow: hidden;
    background: var(--page);
  }
  .billboard {
    position: absolute;
    left: 0;
    top: 420px;
    width: 1200px;
    height: 334px;
    background: var(--forest);
    overflow: hidden;
  }
  .photo {
    position: absolute;
    inset: 0;
    background:
      linear-gradient(90deg, rgba(15,42,28,0) 0%, rgba(15,42,28,0) 45%, rgba(15,42,28,0.85) 65%, var(--forest) 78%),
      linear-gradient(180deg, var(--sky) 0%, #9aa9a8 18%, var(--rock) 34%, #8b8e8f 52%, var(--asphalt) 62%, #2d3033 100%);
  }
  .headline-band {
    position: absolute;
    left: 711px;
    top: 23px;
    width: 379px;
    height: 69px;
    background: var(--orange);
    transform: skewX(-14deg);
  }
  .headline {
    position: absolute;
    left: 735px;
    top: 22px;
    width: 340px;
    font: 58px/70px "Anton", sans-serif;
    color: var(--white);
    text-align: center;
    transform: skewX(-10deg);
    letter-spacing: 0.5px;
  }
  .role {
    position: absolute;
    left: 729px;
    top: 98px;
    font: 27px/34px "Anton", sans-serif;
    color: var(--white);
    transform: skewX(-10deg);
    letter-spacing: 0.3px;
  }
  .pay-band {
    position: absolute;
    left: 862px;
    top: 144px;
    width: 254px;
    height: 81px;
    background: var(--orange);
    transform: skewX(-10deg);
  }
  .pay {
    position: absolute;
    left: 880px;
    top: 142px;
    width: 220px;
    font: 62px/82px "Anton", sans-serif;
    color: var(--white);
    text-align: center;
    transform: skewX(-10deg);
  }
  .pay sup {
    font-size: 22px;
    vertical-align: 28px;
    margin-right: 6px;
  }
  .per-year {
    position: absolute;
    left: 1112px;
    top: 199px;
    font: 22px/28px "Anton", sans-serif;
    color: var(--white);
    transform: skewX(-10deg);
  }
  .phone {
    position: absolute;
    left: 868px;
    top: 240px;
    font: 46px/54px "Anton", sans-serif;
    color: var(--white);
    transform: skewX(-8deg);
    letter-spacing: 1px;
  }
  .website {
    position: absolute;
    left: 870px;
    top: 290px;
    font: italic 700 22px/30px "Open Sans", sans-serif;
    color: var(--white);
  }
  .brand {
    position: absolute;
    left: 33px;
    top: 212px;
    display: flex;
    align-items: center;
    gap: 10px;
  }
  .brand-mark {
    width: 18px;
    height: 18px;
    background: var(--white);
  }
  .brand-name {
    font: 30px/32px "Anton", sans-serif;
    color: var(--white);
    text-transform: uppercase;
    letter-spacing: 1px;
  }
</style>
</head>
<body>
  <section class="billboard" aria-label="Now hiring semi truck drivers billboard">
    <div class="photo" role="img" aria-label="Photo of green semi trucks on a mountain highway with snowy rocky slopes and yellow centre lines"></div>

    <div class="headline-band"></div>
    <div class="headline">NOW HIRING</div>
    <div class="role">SEMI TRUCK DRIVERS</div>

    <div class="pay-band"></div>
    <div class="pay"><sup>$</sup>90,000</div>
    <div class="per-year">A YEAR</div>

    <div class="phone">503-217-6095</div>
    <div class="website">brisklanefreighters.com</div>

    <div class="brand">
      <span class="brand-mark"></span>
      <span class="brand-name">Brisk Lane<br>Freighters</span>
    </div>
  </section>
</body>
</html>
```